Commercial Real Estate Marketing Flyer
Property Highlights
Sir,
I(#21) had given the link, from where you can get my PDF file.
Re#3, I like the footer on the upper right/lower left as it takes less space. I am LOVING the watermark on the bottom right! Can we trying placing it behind the upper right/lower left by shrinking the white box? Then I could decide between the footer or the watermark.
Great stuff!
Can we see what it can look like in a 8.5 x 11 portrait format? I like the footer in #1.
Also on the map page, can we supersize the logo like the footer behind the map?
Good work!
what size do you prefer for the flyer? 8.5x11 landscape? Also, I have no problem in sending the file in publisher format--I've worked with publisher plenty of times.
A Great start!!! Setting the bar pretty high!
As a pdf will be fine. Good luck!
OK, I will send the flyer as a PDF - is this OK?
Henry.
I have had requests for photos and text. What I am looking for is a template that I can use repeatedly for different commercial properties. Just use stock photos and garbled text for now.I am looking for a layout that is clean and current.
The template should be made up of "boxes" where I would fill in text, tables and photos. For example page 1 consists of a photo, bullet points and contact info. Page 2 may contain a table for financial info along with more photo boxes.
Page 3 may be photo and text boxes. Page 4 would be maps along with text and table boxes. hope this helps!!
I have had alot of requests that the final be in Adobe Illustrator and not MS Publisher. To all, that is fine. We want to make it easy for everyone. We will deal with it later. So... go for it!!
Hi, send the text and logo youd like si I can draft up for you thanks...
Please give me your details.Also send me images,texts and other materials that you want to use on your flyer So that I can prepare the Flyer Design for you.
Faris Okoth
Sir I prepare the require design in Adobe Illustrator and if I get success the final file I will provide you in .pdf format. Sir if it is OK then I go a head. Because don't use MS Publisher
Thanks & Regards
Deepak Ruvari
You can see samples of the flyers uploaded in the "Read Brief" section. Good Luck!
please send link of the flyer. Thanks!
Please take a look at the samples we have uploaded along with our new Logo (thanks to IconBrio!). It must be compatible to using MS Publisher. If you want examples of flyers that we like, please private message me and I will link a few flyers.

```html
<!DOCTYPE html>
<html lang="en">
<head>
<meta charset="utf-8">
<title>Norvale Group – Property Flyer</title>
<link href="https://fonts.googleapis.com/css2?family=Open+Sans:wght@400;600;700&family=Playfair+Display:ital,wght@1,600&display=swap" rel="stylesheet">
<style>
:root{
  --bg:#e7e4df;
  --navy:#0d2563;
  --blue:#1a4a9e;
  --blue-mid:#2e67c0;
  --sky:#5d8fd8;
  --ink:#2b2f36;
  --muted:#6b717b;
  --paper:#ffffff;
  --rule:#d5dae3;
}
*{box-sizing:border-box;margin:0;padding:0}
html,body{width:1200px;height:897px;overflow:hidden}
body{background:var(--bg);font-family:"Open Sans",Arial,sans-serif;color:var(--ink);position:relative}
.spread{position:absolute;left:288px;width:624px;height:420px;display:flex;box-shadow:0 6px 18px rgba(0,0,0,.22)}
.spread--outer{top:18px}
.spread--inner{top:458px}
.page{position:relative;width:312px;height:420px;overflow:hidden;background:var(--paper)}

/* brand */
.brand{display:flex;align-items:center;gap:6px}
.brand__dot{width:22px;height:22px;border-radius:50%;background:var(--blue)}
.brand__name{font-weight:700;font-size:13px;letter-spacing:.5px;color:var(--blue)}
.watermark{position:absolute;font-weight:700;color:rgba(255,255,255,.12);letter-spacing:2px;white-space:nowrap}

/* cover */
.cover .brand{position:absolute;left:20px;top:28px}
.cover__photo{position:absolute;left:0;top:72px;width:312px;height:228px;background:linear-gradient(180deg,#cfdcea 0%,#e8eef4 38%,#b9b3a6 55%,#7d9a5a 75%,#5f7f3e 100%)}
.cover__band{position:absolute;left:0;bottom:0;width:312px;height:120px;background:linear-gradient(135deg,var(--blue) 0%,var(--navy) 100%)}
.cover__band::before{content:"";position:absolute;left:0;top:0;width:100%;height:4px;background:var(--sky)}
.cover__note{position:absolute;left:14px;top:16px;width:170px;font-size:5.5px;line-height:1.5;color:#dfe8f7}
.cover .watermark{right:10px;bottom:8px;font-size:30px}

/* map page */
.locale{background:linear-gradient(160deg,var(--blue) 0%,var(--navy) 70%)}
.locale__arc{position:absolute;inset:0}
.highlights{position:absolute;left:14px;top:16px;width:124px;list-style:none}
.highlights li{font-size:6px;line-height:1.35;color:#e6eefb;padding-left:7px;position:relative;margin-bottom:4px}
.highlights li::before{content:"";position:absolute;left:0;top:3px;width:3px;height:3px;background:#fff;border-radius:50%}
.locale__map{position:absolute;left:148px;top:16px;width:150px;height:150px;background:linear-gradient(135deg,#f1ead6,#e3d9bd);border:2px solid #fff}
.locale .watermark{left:190px;top:170px;font-size:64px;color:rgba(255,255,255,.08)}
.locale .brand{position:absolute;left:112px;top:232px}
.locale .brand__dot{background:#fff}
.locale .brand__name{color:#fff}
.contact{position:absolute;left:112px;top:290px;color:#fff}
.contact__name{font-size:9px;font-weight:600;letter-spacing:.5px;margin-bottom:8px}
.contact p{font-size:6.5px;line-height:1.5}

/* inner pages */
.tab{position:absolute;left:0;top:18px;height:18px;padding:0 14px 0 8px;display:flex;align-items:center;gap:5px;background:linear-gradient(90deg,var(--navy),var(--blue-mid));border-radius:0 9px 9px 0;color:#fff;font-size:8px;font-weight:700}
.tab__dot{width:9px;height:9px;border-radius:50%;background:#fff}
.summary__title{position:absolute;left:14px;top:44px;font-family:"Playfair Display",Georgia,serif;font-style:italic;font-size:18px;color:var(--ink)}
.summary__intro{position:absolute;left:14px;top:72px;width:284px;font-size:5.5px;line-height:1.5;color:var(--muted)}
.specs{position:absolute;left:14px;top:104px;width:128px;font-size:5.5px}
.specs div{display:flex;justify-content:space-between;padding:2px 0;border-bottom:1px solid var(--rule)}
.specs dt{color:var(--muted)}
.specs dd{font-weight:600}
.summary__photo{position:absolute;left:160px;top:104px;width:138px;height:92px;background:linear-gradient(180deg,#d4dfe9 0%,#9fb08b 55%,#5f7f3e 100%);border:1px solid var(--rule)}
.rent-roll{position:absolute;left:14px;top:222px;width:284px;border-collapse:collapse;font-size:5px}
.rent-roll th{background:var(--blue);color:#fff;font-weight:600;padding:4px 2px;text-align:center}
.rent-roll td{padding:4px 2px;text-align:center;border-bottom:1px solid var(--rule)}
.rent-roll tr:nth-child(even) td{background:#f1f4f9}
.rent-roll .total td{font-weight:700}
.footer-band{position:absolute;left:0;bottom:0;width:312px;height:30px;background:linear-gradient(90deg,var(--navy),var(--blue-mid))}
.footer-band__url{position:absolute;left:14px;top:10px;font-size:7px;color:#fff;font-weight:600}
.footer-band .watermark{right:10px;top:2px;font-size:20px}

.market__ring{position:absolute;right:-70px;top:110px;width:260px;height:260px;border-radius:50%;border:28px solid rgba(46,103,192,.08)}
.market__list{position:absolute;left:14px;top:48px;width:284px}
.market__item{display:flex;gap:8px;margin-bottom:10px}
.market__photo{flex:0 0 62px;height:54px;border:1px solid var(--rule)}
.market__item p{font-size:5.5px;line-height:1.55;color:var(--muted)}
.market__item strong{color:var(--blue)}
</style>
</head>
<body>

<section class="spread spread--outer">
  <article class="page cover">
    <div class="brand"><span class="brand__dot"></span><span class="brand__name">NORVALE GROUP</span></div>
    <div class="cover__photo" role="img" aria-label="Photo of the apartment community entrance with monument sign, lawn and trees"></div>
    <div class="cover__band">
      <p class="cover__note">All information provided is deemed reliable but is not guaranteed and should be independently verified by buyer.</p>
      <span class="watermark">NORVALE</span>
    </div>
  </article>

  <article class="page locale">
    <svg class="locale__arc" viewBox="0 0 312 420" aria-hidden="true"><path d="M0 360 Q160 250 312 300" fill="none" stroke="rgba(255,255,255,.08)" stroke-width="40"/></svg>
    <ul class="highlights">
      <li>Prime retail location</li>
      <li>Close to freeway access</li>
      <li>High traffic corridor daily</li>
      <li>Ample on-site parking spaces</li>
      <li>Near major shopping centers</li>
      <li>Stable long-term tenants</li>
      <li>Strong area demographics</li>
      <li>Walking distance to schools</li>
      <li>Recent exterior renovations</li>
      <li>Flexible lease terms available</li>
    </ul>
    <span class="watermark">NVG</span>
    <div class="locale__map" role="img" aria-label="Street map of the surrounding area showing the property location"></div>
    <div class="brand"><span class="brand__dot"></span><span class="brand__name">NORVALE GROUP</span></div>
    <div class="contact">
      <p class="contact__name">NORVALE GROUP</p>
      <p>2180 W Larkspur Ave, Suite 204, Tellmont, CA 90417</p>
      <p>Phone 555-201-4830 Fax 555-201-4831</p>
    </div>
  </article>
</section>

<section class="spread spread--inner">
  <article class="page summary">
    <div class="tab"><span class="tab__dot"></span>Investment Summary</div>
    <h1 class="summary__title">The Willows</h1>
    <p class="summary__intro">The Willows is a well maintained residential community located in a growing neighborhood, offering investors steady income, strong occupancy and long term appreciation potential in a desirable market.</p>
    <dl class="specs">
      <div><dt>Price</dt><dd>$4,250,000</dd></div>
      <div><dt>Units</dt><dd>64</dd></div>
      <div><dt>Price/Unit</dt><dd>$66,406</dd></div>
      <div><dt>Cap Rate</dt><dd>7.2%</dd></div>
      <div><dt>Year Built</dt><dd>1986</dd></div>
      <div><dt>Lot Size</dt><dd>3.1 Acres</dd></div>
      <div><dt>Occupancy</dt><dd>96%</dd></div>
      <div><dt>Parking</dt><dd>120 Spaces</dd></div>
      <div><dt>Zoning</dt><dd>R-3</dd></div>
    </dl>
    <div class="summary__photo" role="img" aria-label="Photo of the property monument sign surrounded by landscaping"></div>
    <table class="rent-roll">
      <thead><tr><th>Unit Type</th><th>Units</th><th>Sq Ft</th><th>Rent</th><th>Monthly Income</th><th>Annual Income</th><th>Rent/SF</th></tr></thead>
      <tbody>
        <tr><td>1 Bed/1 Bath</td><td>16</td><td>650</td><td>$695</td><td>$11,120</td><td>$133,440</td><td>$1.07</td></tr>
        <tr><td>2 Bed/1 Bath</td><td>24</td><td>850</td><td>$825</td><td>$19,800</td><td>$237,600</td><td>$0.97</td></tr>
        <tr><td>2 Bed/2 Bath</td><td>16</td><td>950</td><td>$895</td><td>$14,320</td><td>$171,840</td><td>$0.94</td></tr>
        <tr><td>3 Bed/2 Bath</td><td>8</td><td>1,150</td><td>$1,050</td><td>$8,400</td><td>$100,800</td><td>$0.91</td></tr>
        <tr class="total"><td>Total</td><td>64</td><td>56,000</td><td>—</td><td>$53,640</td><td>$643,680</td><td>$0.96</td></tr>
      </tbody>
    </table>
    <div class="footer-band"><span class="footer-band__url">www.norvalegrp.com</span><span class="watermark">NORVALE</span></div>
  </article>

  <article class="page market">
    <div class="market__ring" aria-hidden="true"></div>
    <div class="tab"><span class="tab__dot"></span>Market Overview</div>
    <div class="market__list">
      <div class="market__item"><div class="market__photo" role="img" aria-label="Photo of a residential street" style="background:linear-gradient(180deg,#cdd9e6,#8ea473)"></div><p><strong>Tellmont Overview:</strong> The city remains one of the fastest growing areas in the region, with steady job growth and rising household incomes.</p></div>
      <div class="market__item"><div class="market__photo" role="img" aria-label="Photo of an office building" style="background:linear-gradient(180deg,#b9c9dc,#9a8a72)"></div><p><strong>Employment:</strong> Major employers in healthcare, education and logistics anchor the local economy and support consistent demand for rental housing nearby.</p></div>
      <div class="market__item"><div class="market__photo" role="img" aria-label="Photo of a neighborhood home" style="background:linear-gradient(180deg,#d6e0ea,#a6a08a)"></div><p><strong>Rental Market:</strong> Area vacancy rates stay below five percent while average rents have increased each year over the past decade.</p></div>
      <div class="market__item"><div class="market__photo" role="img" aria-label="Photo of mountains and a lake" style="background:linear-gradient(180deg,#9fbbe0,#5f7f6a)"></div><p><strong>Recreation:</strong> Residents enjoy nearby parks, lakes and mountain trails, along with dining, shopping and entertainment within a short drive.</p></div>
      <div class="market__item"><div class="market__photo" role="img" aria-label="Photo of a commercial development" style="background:linear-gradient(180deg,#d2dce8,#8f9a7a)"></div><p><strong>Development:</strong> New commercial projects and road improvements planned for the corridor are expected to add value to surrounding properties.</p></div>
    </div>
  </article>
</section>

</body>
</html>
```